Business card design needed for Automotive Reconditioning business

I have a logo design i just cant decide on the best color or layout for the business card, I will upload all the files so you can see all colors schemes we are considering. I have other file formats if needed let me know.

Target Market(s)

automotive dealerships

Contact Information for Business Card

HERE are the Descriptions and info needed on the card:
Interior Repair: Leather carpet burns panels dash Deoderize
Dealer products and Vin Verify
( spot for name and cell number) My name is Dorian Pelk phone 951 430-2158 Title COO www.BrolvexMotor.com

Font styles to use
Sans Serif
Other font styles liked:
• what ever you think looks best

Requirements
Must have
• Must be able to change the name and phone for employees

```html
<!DOCTYPE html>
<html lang="en">
<head>
<meta charset="utf-8">
<title>Brolvex Motor Reconditioning – Business Card</title>
<link rel="stylesheet" href="https://fonts.googleapis.com/css2?family=Roboto:wght@400;700;900&family=Cinzel:wght@600&display=swap">
<style>
  :root {
    --stage: #3b3b3d;
    --card-black: #0c0c0d;
    --band-red: #e0262b;
    --mesh-dark: #1c1c1e;
    --mesh-light: #2e2f33;
    --text-white: #ffffff;
    --text-soft: #d9d9d9;
    --accent-blue: #2f8fd6;
    --splash-red: #d8232a;
    --splash-grey: #8a8a8f;
  }
  * { box-sizing: border-box; margin: 0; padding: 0; }
  html, body {
    width: 1200px; height: 716px; overflow: hidden;
    background: var(--stage);
    font-family: "Roboto", Arial, sans-serif;
  }
  .canvas {
    position: relative; width: 1200px; height: 716px;
    display: flex; align-items: center; justify-content: center; gap: 60px;
  }
  .card {
    position: relative; width: 520px; height: 297px;
    background: var(--card-black); overflow: hidden;
    border-radius: 4px;
    box-shadow: 0 14px 30px rgba(0,0,0,.45);
  }

  /* Front card */
  .front__mesh {
    position: absolute; left: 0; top: 0; width: 100%; height: 170px;
    background: radial-gradient(ellipse at 75% 30%, var(--mesh-light), var(--mesh-dark) 70%);
  }
  .front__band {
    position: absolute; left: 0; top: 42px; width: 58%; height: 128px;
    background: var(--band-red);
    display: flex; align-items: center; justify-content: center;
  }
  .front__band-tail {
    position: absolute; left: 58%; top: 42px; width: 42%; height: 128px;
    background: linear-gradient(90deg, var(--band-red), rgba(224,38,43,0) 80%);
  }
  .brand-name {
    font-family: "Roboto", Arial, sans-serif; font-weight: 900;
    color: var(--text-white); font-size: 34px; letter-spacing: 1px;
    line-height: 1; text-transform: uppercase; text-align: center;
  }
  .front .brand-name { position: absolute; left: 0; top: 42px; width: 100%; height: 128px;
    display: flex; align-items: center; justify-content: center; }
  .front__services {
    position: absolute; left: 0; top: 196px; width: 100%;
    color: var(--text-white); font-size: 15px; line-height: 1.45; text-align: center;
    padding: 0 30px;
  }

  /* Back card */
  .back .brand-name {
    position: absolute; left: 30px; top: 40px; font-size: 30px; text-align: left;
  }
  .back__person { position: absolute; left: 30px; top: 120px; color: var(--text-white); }
  .person-name {
    font-family: "Cinzel", Georgia, serif; font-weight: 600; font-size: 19px; letter-spacing: 1px;
  }
  .person-title { font-size: 13px; margin-top: 6px; color: var(--text-soft); }
  .back__phone {
    position: absolute; left: 30px; top: 200px;
    display: flex; align-items: center; gap: 10px;
    color: var(--text-white); font-size: 13px;
  }
  .phone-icon { width: 18px; height: 18px; display: block; }
  .back__splash {
    position: absolute; right: 10px; bottom: 0; width: 290px; height: 200px;
    background:
      radial-gradient(ellipse at 70% 45%, var(--splash-red), rgba(216,35,42,0) 55%),
      radial-gradient(ellipse at 40% 50%, var(--splash-grey), rgba(138,138,143,0) 60%);
  }
</style>
</head>
<body>
<main class="canvas">

  <section class="card front" aria-label="Card front">
    <div class="front__mesh" role="img" aria-label="Dark perforated metal mesh texture"></div>
    <div class="front__band"></div>
    <div class="front__band-tail"></div>
    <div class="brand-name">Brolvex Motor</div>
    <p class="front__services">
      Interior Repair: Leather carpet burns panels dash Deoderize<br>
      Dealer products and Vin Verify
    </p>
  </section>

  <section class="card back" aria-label="Card back">
    <div class="brand-name">Brolvex Motor</div>
    <div class="back__person">
      <p class="person-name">Dorian Pelk</p>
      <p class="person-title">COO</p>
    </div>
    <div class="back__phone">
      <svg class="phone-icon" viewBox="0 0 18 18" aria-hidden="true">
        <circle cx="9" cy="9" r="9" fill="var(--accent-blue)"/>
        <path d="M6.2 4.6l1.4-.3 1 2.3-.9.8a6 6 0 0 0 2.9 2.9l.8-.9 2.3 1-.3 1.4c-.1.4-.5.7-.9.6A8 8 0 0 1 5.6 5.5c-.1-.4.2-.8.6-.9z" fill="#fff"/>
      </svg>
      <span>951 430-2158</span>
    </div>
    <div class="back__splash" role="img" aria-label="White sports car bursting through red and grey paint splash"></div>
  </section>

</main>
</body>
</html>
```